Bluerock Data Partners - IT Support Tri-Fold

Need a tri-fold brochure for marketing, pitching managed IT Services. These services include computer/server management, security, cloud backups. The tri-fold should use our logo and colors (Attached)

```html
<!DOCTYPE html>
<html lang="en">
<head>
<meta charset="utf-8">
<title>Bluerock Data Partners – IT Support Tri-Fold</title>
<link href="https://fonts.googleapis.com/css2?family=Raleway:wght@300;400;500;600&family=Open+Sans:wght@400;600&display=swap" rel="stylesheet">
<style>
:root{
  --bg:#c8c8c8;
  --blue:#3d55b8;
  --blue-dark:#2f45a0;
  --red:#d6262b;
  --green:#3aa63f;
  --white:#ffffff;
  --ink:#2b2b2b;
  --grey-panel:#eeeeee;
  --photo-office:#5f6b7a;
  --photo-red:#c8242a;
}
*{margin:0;padding:0;box-sizing:border-box}
html,body{width:1200px;height:4408px;overflow:hidden}
body{background:var(--bg);font-family:'Open Sans',sans-serif;color:var(--ink);position:relative}
.spread{position:absolute;left:50px;width:1100px;height:786px;background:var(--white);overflow:hidden;box-shadow:0 6px 24px rgba(0,0,0,.18)}
.spread--outside{top:1388px}
.spread--inside{top:2234px}
.abs{position:absolute}

/* outside */
.red-band{left:0;top:0;width:83px;height:786px;background:linear-gradient(180deg,#e0393c,var(--red) 60%,#b81d22)}
.blue-field{left:83px;top:0;width:762px;height:786px;background:var(--blue)}
.why-heading{left:115px;top:42px;font-family:'Raleway',sans-serif;font-weight:300;font-size:35px;line-height:46px;color:var(--white);letter-spacing:1px}
.why-copy{left:115px;top:264px;width:222px;font-size:12.2px;line-height:16px;color:var(--white)}
.why-copy p{margin-bottom:14px}
.photo-team{left:365px;top:161px;width:735px;height:374px;background:linear-gradient(120deg,#e9ecef 0%,#b9c0c8 35%,var(--photo-office) 70%,#3f4753 100%)}
.brand-panel{left:845px;top:0;width:255px;height:161px;background:var(--white)}
.tagline-panel{left:845px;top:535px;width:255px;height:251px;background:var(--white)}
.brand{display:flex;align-items:center;gap:8px;font-family:'Raleway',sans-serif;font-weight:600;color:var(--blue-dark)}
.brand-mark{width:16px;height:16px;background:var(--blue-dark);flex:none}
.brand--top{left:868px;top:52px;font-size:19px;line-height:24px;width:220px}
.brand--mid{left:418px;top:572px;font-size:18px;color:var(--white);line-height:22px;width:230px}
.brand--mid .brand-mark{background:var(--white)}
.contact{left:440px;top:640px;font-size:12.4px;line-height:21px;color:var(--white)}
.contact-line{display:flex;align-items:center;gap:7px}
.contact-line svg{flex:none}
.web-bar{height:24px;background:var(--green);color:var(--white);font-size:13px;line-height:24px;text-align:center}
.web-bar--mid{left:440px;top:716px;width:224px}
.web-bar--right{left:876px;top:716px;width:224px}
.tagline{left:876px;top:568px;font-family:'Raleway',sans-serif;font-weight:500;font-size:35px;line-height:44px;color:var(--ink)}

/* inside */
.story{left:0;top:0;width:376px;height:463px;padding:28px 34px 0 38px;background:var(--white)}
.section-title{font-family:'Raleway',sans-serif;font-weight:400;font-size:32px;color:var(--ink);letter-spacing:.5px;margin-bottom:16px}
.story p{font-size:10.4px;line-height:13.3px;margin-bottom:10px;letter-spacing:-.1px}
.services{left:376px;top:0;width:364px;height:463px;background:var(--blue);padding:48px 40px 0 42px;color:var(--white)}
.service{margin-bottom:34px}
.service h3{font-family:'Raleway',sans-serif;font-weight:400;font-size:17px;letter-spacing:.5px;margin-bottom:10px}
.service p{font-size:10.4px;line-height:13.3px}
.photo-cloud{left:740px;top:0;width:360px;height:463px;background:radial-gradient(circle at 55% 40%,#f28a83 0%,#e24a44 30%,var(--photo-red) 60%,#8e1619 100%)}
.photo-meeting{left:0;top:463px;width:376px;height:323px;background:linear-gradient(180deg,#eef0f3 0%,#c5c9d0 45%,#5b606b 80%,#2d3038 100%)}
.reviews{left:376px;top:463px;width:724px;height:323px;background:var(--grey-panel)}
.reviews-title{left:0;width:724px;top:16px;text-align:center;font-family:'Raleway',sans-serif;font-weight:400;font-size:32px;letter-spacing:.5px;color:var(--ink)}
.review{top:82px;width:300px;font-size:10.4px;line-height:13.3px}
.review--one{left:42px}
.review--two{left:382px}
.quote{font-family:Georgia,serif;font-size:34px;line-height:20px;color:var(--green);font-weight:700}
.quote--open{position:absolute;left:-30px;top:4px}
.quote--close{display:block;text-align:right;margin-top:-2px}
.reviewer{margin-top:4px;padding-left:120px;font-size:10px;line-height:12.5px}
.reviewer strong{color:var(--blue-dark);font-weight:600;text-transform:uppercase}
</style>
</head>
<body>

<section class="spread spread--outside" aria-label="Brochure outside spread">
  <div class="abs red-band"></div>
  <div class="abs blue-field"></div>

  <h2 class="abs why-heading">WHY<br>PEOPLE<br>CHOOSE<br>US</h2>
  <div class="abs why-copy">
    <p>Since 2015, Bluerock Data Partners has provided Southern New England with on-site, and remote technical support services. We primarily serve eastern Connecticut, Rhode Island, and Southern Massachusetts.</p>
    <p>We pride ourselves on industry-leading response time, with a focus on customer service. When you call our office, a real representative in Connecticut will answer, not an outsourced answering system.</p>
    <p>With over 30 years of combined experience across our team, we work to provide real solutions to you - whether you need help fixing your home's computer, need one hundred computers upgraded for your business, or are looking to build a website - we will explain the technology to you in a language you understand, and provide a personalized solution for your unique situation.</p>
  </div>

  <div class="abs brand-panel"></div>
  <div class="abs brand brand--top"><span class="brand-mark"></span>Bluerock Data Partners</div>

  <div class="abs photo-team" role="img" aria-label="Photo of a team of colleagues gathered around a computer monitor in an office"></div>
  <svg class="abs" style="left:845px;top:153px" width="255" height="8" aria-hidden="true">
    <rect x="0" y="0" width="85" height="8" fill="#3d55b8"/><rect x="85" y="0" width="85" height="8" fill="#3aa63f"/><rect x="170" y="0" width="85" height="8" fill="#d6262b"/>
  </svg>
  <svg class="abs" style="left:845px;top:535px" width="255" height="8" aria-hidden="true">
    <rect x="0" y="0" width="85" height="8" fill="#3d55b8"/><rect x="85" y="0" width="85" height="8" fill="#3aa63f"/><rect x="170" y="0" width="85" height="8" fill="#d6262b"/>
  </svg>

  <div class="abs brand brand--mid"><span class="brand-mark"></span>Bluerock Data Partners</div>
  <div class="abs contact">
    <div class="contact-line"><svg width="11" height="11" viewBox="0 0 24 24" aria-hidden="true"><path fill="#fff" d="M6.6 10.8a15.1 15.1 0 0 0 6.6 6.6l2.2-2.2a1 1 0 0 1 1-.25 11.4 11.4 0 0 0 3.6.57 1 1 0 0 1 1 1V20a1 1 0 0 1-1 1A17 17 0 0 1 3 4a1 1 0 0 1 1-1h3.5a1 1 0 0 1 1 1c0 1.25.2 2.45.57 3.57a1 1 0 0 1-.25 1z"/></svg>+1 401-555-0187</div>
    <div class="contact-line">info@bluerockdata.solutions</div>
    <div class="contact-line"><svg width="11" height="11" viewBox="0 0 24 24" aria-hidden="true"><path fill="#fff" d="M12 2a7 7 0 0 0-7 7c0 5.25 7 13 7 13s7-7.75 7-13a7 7 0 0 0-7-7zm0 9.5A2.5 2.5 0 1 1 12 6.5a2.5 2.5 0 0 1 0 5z"/></svg>42 Harbor Lane, Millbrook CT 06400</div>
  </div>
  <div class="abs web-bar web-bar--mid">www.bluerockdata.solutions</div>

  <div class="abs tagline-panel"></div>
  <h1 class="abs tagline">REAL<br>BUSINESS<br>SOLUTIONS</h1>
  <div class="abs web-bar web-bar--right">www.bluerockdata.solutions</div>
</section>

<section class="spread spread--inside" aria-label="Brochure inside spread">
  <div class="abs story">
    <h2 class="section-title">OUR STORY</h2>
    <p>Bluerock Data Partners was founded in 2015 by Owen Hartley in Cedar Point, RI, providing small residential services to local residents. Over the years, BDP has grown into a full service business, providing service to clients as far as California and Texas, with regular on-site service in Boston, Hartford, and New York. In 2017, Bluerock Data Partners graduated from the basement and moved to our first location in Alder Cove, CT - at the Linen Mill. Soon, our daily operations out-grew the small office location and we moved to our current home in 2019 – in Millbrook, CT. We now operate a fleet of vehicles with staff for on-site appointments for our regular business and residential clients.</p>
    <p>Our mission is to make tech work for people, rather than against them. As a full-service technology firm, our services range from on-site business and residential tech support and troubleshooting, to online web services such as web hosting, web design, and e-mail hosting. Whatever your technology needs, Bluerock Data Partners has the solution for you.</p>
    <p>We provide all facets of IT Service, from on-site business and residential support and troubleshooting, to installs and setups of varied equipment, and online web services such as hosting and web design. Whatever your technology needs, Bluerock Data Partners has the solution for you.</p>
  </div>

  <div class="abs services">
    <div class="service">
      <h3>RESIDENTIAL SERVICES</h3>
      <p>We've got the experience and knowledge to solve your residential tech needs. We have been serving residents of CT &amp; RI since 2015, and have strived to make the world of technology easier and less stressful for our clients.</p>
    </div>
    <div class="service">
      <h3>BUSINESS SERVICES</h3>
      <p>We've got the experience and knowledge to solve your business tech needs. We have been serving residents of CT &amp; RI since 2015, and have strived to make the world of technology easier and less stressful for our clients.</p>
    </div>
    <div class="service">
      <h3>WEB SERVICES</h3>
      <p>We have the experience and knowledge to improve your business with web services. We've got solid experience in web design, email services, search optimization and more. We'll work with you to grow your online presence, and grow your business.</p>
    </div>
  </div>

  <div class="abs photo-cloud" role="img" aria-label="Red-toned photo of hands typing on a laptop with a glowing cloud network of connected icons above"></div>
  <div class="abs photo-meeting" role="img" aria-label="Backlit photo of business people in silhouette seated around a meeting table by bright windows"></div>

  <div class="abs reviews">
    <h2 class="abs reviews-title">WHAT CUSTOMERS SAY</h2>
    <div class="abs review review--one">
      <span class="quote quote--open">“</span>
      <p>Owen and his team are extremely professional, friendly and knowledgeable. Bluerock Data has been able to fix all issues that have arisen within a very timely manner, usually within a couple of hours. They were even able to solve issues that our previous IT company could not. We now have an annual service contract with Bluerock Data. I would highly recommend Owen and his team at Bluerock Data. I have not run into a problem that they cannot solve, and I don't think that you will either.</p>
      <span class="quote quote--close">”</span>
      <div class="reviewer"><strong>Dana Whitfield</strong><br>Vice President, Whitfield Fuel<br>Harbor Falls, CT</div>
    </div>
    <div class="abs review review--two">
      <span class="quote quote--open">“</span>
      <p>If you are ever in need of some cutting edge website ideas and first-class execution for your e-commerce marketing efforts, Bluerock Data Partners is the business partner you want to work with. BDP is much more than a website design company. The team is up-to-date with the pulse of digital trends and have a commitment to the industry's best practices. I couldn't recommend them more strongly. You owe it to your business to contact them for your next online project.</p>
      <span class="quote quote--close">”</span>
      <div class="reviewer"><strong>Marcus Lindqvist</strong><br>Senior Partner, Lindqvist &amp; Co.<br>Los Angeles &amp; Silicon Valley, CA</div>
    </div>
  </div>
</section>

</body>
</html>
```